GPS Tracker Business Card Design

We need a business card for a GPS Vehicle tracking company. We sell the hardware for the vehicle and the software platform to monitor your vehicle/s. Including high asset non-powered vehicles like a trailer using our solar powered unit.
We like using dark blue to different shades of blue along with gold. We have phone apps for Android and Apple devices.

We have a platform for families wanting to track their teenage driver and children; Plus a Fleet vehicle tracking platform.

Features: unlimited number of vehicles and/or assets including snow mobiles forklifts generators trailers airport equipment

Reports for driving behavior reports and alerts dashboard fleet maintenace timeline view and replay geofence real time alerts logbook scheduling route optimization accounting integration fleet grouping closest vehicle locator On Board Diagnostics.

Benefits: Increased productivity improved fuel efficiency organizing your business improve time management simplify back end processes, reduce fleet fuel efficiency and expenses increase fleet security etc..

Please view website: Velmora.com

Industry/Entity Type

Business

Contact Information for Business Card

Harold B Pennick

```html
<!DOCTYPE html>
<html lang="en">
<head>
<meta charset="UTF-8">
<title>Velmora Business Card</title>
<link href="https://fonts.googleapis.com/css2?family=Open+Sans:wght@300;400;600&display=swap" rel="stylesheet">
<style>
  :root {
    --stage: #e9e7e4;
    --card-white: #ffffff;
    --brand-blue: #0f52a0;
    --accent-blue: #1a5aa6;
    --ink-dark: #1b1b1b;
    --ink-grey: #6a6a6a;
    --rule-grey: #a9a9a9;
    --map-faint: rgba(225,228,232,0.55);
    --map-dots: rgba(90,140,200,0.55);
  }
  * { margin: 0; padding: 0; box-sizing: border-box; }
  html, body {
    width: 1200px; height: 1000px; overflow: hidden;
    background: var(--stage);
    font-family: "Open Sans", sans-serif;
  }
  .canvas { position: relative; width: 1200px; height: 1000px; }

  .card {
    position: absolute; left: 265px; width: 665px; height: 397px;
    border-radius: 24px; overflow: hidden;
    box-shadow: 0 6px 16px rgba(0,0,0,0.18);
  }
  .card--front { top: 73px; background: var(--card-white); }
  .card--back { top: 532px; background: var(--brand-blue); }

  .map-area { position: absolute; }
  .card--front .map-area {
    left: 90px; top: 30px; width: 560px; height: 320px;
    background: radial-gradient(ellipse closest-side at center, var(--map-faint) 0%, transparent 100%);
  }
  .card--back .map-area {
    left: 20px; top: 26px; width: 570px; height: 320px;
    background: radial-gradient(ellipse closest-side at center, var(--map-dots) 0%, transparent 100%);
  }

  .wordmark {
    position: absolute; font-weight: 300; letter-spacing: -1px; line-height: 1;
  }
  .card--front .wordmark { left: 32px; top: 52px; font-size: 64px; color: var(--ink-dark); }
  .card--back .wordmark { right: 50px; top: 272px; font-size: 64px; color: var(--card-white); }

  .tagline {
    position: absolute; left: 49px; top: 124px;
    font-size: 19px; color: var(--ink-grey); font-weight: 400;
  }

  .holder { position: absolute; right: 32px; top: 211px; text-align: right; }
  .holder__name { font-size: 21px; font-weight: 600; color: var(--accent-blue); line-height: 1.2; }
  .holder__title { font-size: 15.5px; color: var(--ink-grey); margin-top: 4px; }

  .rule {
    position: absolute; left: 32px; top: 250px; width: 444px; height: 2px;
    background: var(--rule-grey);
  }

  .contact-list { position: absolute; left: 32px; top: 272px; list-style: none; }
  .contact-list li {
    display: flex; align-items: center; gap: 7px;
    height: 23.5px; font-size: 16px; color: var(--ink-grey);
  }
  .contact-list svg { width: 16px; height: 16px; fill: var(--accent-blue); flex: none; }

  .address {
    position: absolute; right: 32px; top: 313px; text-align: right;
    font-size: 16px; line-height: 23.5px; color: var(--ink-grey); font-style: normal;
  }

  .web {
    position: absolute; right: 36px; top: 346px;
    font-size: 18px; letter-spacing: 5.5px; color: var(--card-white);
  }
</style>
</head>
<body>
<main class="canvas">

  <section class="card card--front" aria-label="Card front">
    <div class="map-area" role="img" aria-label="Faint grey world map in the background"></div>
    <div class="wordmark">Velmora</div>
    <p class="tagline">Every Road, Every Mile</p>

    <div class="holder">
      <p class="holder__name">Harold B Pennick</p>
      <p class="holder__title">Managing Parthner</p>
    </div>
    <div class="rule"></div>

    <ul class="contact-list">
      <li>
        <svg viewBox="0 0 16 16" aria-hidden="true"><path d="M2 6c0-2 2-3 6-3s6 1 6 3v1h-3V5.5H5V7H2zM4 8h8l1.5 5h-11z"/></svg>
        + 000 000 0000
      </li>
      <li>
        <svg viewBox="0 0 16 16" aria-hidden="true"><path d="M4 2h8v3H4zM1 6h14v6h-3v-2H4v2H1zM5 11h6v3H5z"/></svg>
        + 000 000 0000
      </li>
      <li>
        <svg viewBox="0 0 16 16" aria-hidden="true"><path d="M1 4h14v1l-7 4.5L1 5zM1 6.5l7 4.5 7-4.5V12H1z"/></svg>
        info@Velmora.com
      </li>
      <li>
        <svg viewBox="0 0 16 16" aria-hidden="true"><path d="M8 1a7 7 0 1 0 0 14A7 7 0 0 0 8 1zm0 1.6c.8 1 1.3 2.3 1.4 3.6H6.6C6.7 4.9 7.2 3.6 8 2.6zM2.7 7.4h2.6c.1 1.3.5 2.6 1.2 3.6a5.4 5.4 0 0 1-3.8-3.6zm3.9 0h2.8c-.1 1.4-.6 2.6-1.4 3.6-.8-1-1.3-2.2-1.4-3.6zm4.1 0h2.6a5.4 5.4 0 0 1-3.8 3.6c.7-1 1.1-2.3 1.2-3.6z"/></svg>
        www.Velmora.com
      </li>
    </ul>

    <address class="address">
      215 Corrigan Valley Rd<br>
      Ashbrook, QLD, 4218
    </address>
  </section>

  <section class="card card--back" aria-label="Card back">
    <div class="map-area" role="img" aria-label="Dotted world map in lighter blue"></div>
    <div class="wordmark">Velmora</div>
    <p class="web">www.Velmora.com</p>
  </section>

</main>
</body>
</html>
```